A SEASON OF EMBERS book cover needed

Hello friends! I'm working toward self-publishing my first novel in the next few months, and I'm looking to have a professional-looking, 6 in x 9 in cover to go along with the ebook release. I’m not looking for much, but the key is that it must look professional. I don’t want decorative fonts, but I also don’t want it to just look like Helvetica or Times New Roman.The text for the cover should be:A TIME FOR GREATNESSKARLIS WILDEI have attached a few images to show you where my head is at. I created a book cover myself on paint that looks horribly amateur, but it draws inspiration from a HPB campaign poster(also attached) where the title of the novel comes from. If you can make that same kind of cover, but make it look professional, that would be amazing! If you have other, simple ideas, I am also very, very open.Attached as well are a couple of simple, recent book covers that I like. That is the kind of thing that I am looking for.If this goes well, I may do a paperback release. In that case, I may need to contact you again for an additional fee to create the rest of the wraparound design. In addition, the book is the first in a projected trilogy, so there may be opportunities for you in the future for sequel covers.About the book: A SEASON OF EMBERS is a gripping, standalone thriller with an exciting take on history, relationships, conspiracy theories, and the current, volatile political state of America. In the present day, new information surrounding the 1963 assassination of Harold P. Brisbane comes to light and Milo Fenwright, a young, best-selling journalist still reconciling his success with his dark past, finds himself more personally connected than he ever could have expected. But the story becomes something even bigger when an assassination attempt on the current demagogic president sends the whole world of journalism into a scramble, and Milo finds himself confronted by an extremely difficult question: Is democracy real, or has it been an illusion fostered by these secretive ‘Stewards of the Union’ since 1776? Travelling across Syria, Canada, and the United States of America, the story becomes more unbelievable—and more personal—as increasingly prominent figures begin to enter Milo’s orbit, intent on keeping their secrets safe by whatever means necessary.

Colors

Designer to choose colors to be used in the design.

Requirements
Must have
• Text
• Simplicity
• Professional look
Should not have
• Cheap fonts
• Complicated images

```html
<!DOCTYPE html>
<html lang="en">
<head>
<meta charset="utf-8">
<title>A Season of Embers — Tomas Reyvik</title>
<link href="https://fonts.googleapis.com/css2?family=Oswald:wght@300;400;500;600&display=swap" rel="stylesheet">
<style>
  :root {
    --red-deep: #2a0405;
    --red-dark: #5e0a0c;
    --red-mid: #a3141a;
    --red-glow: #e5262b;
    --title-silver: #e4e4e6;
    --author-grey: #d6d6d8;
    --rule-grey: rgba(220, 220, 222, 0.75);
  }
  * { margin: 0; padding: 0; box-sizing: border-box; }
  html, body {
    width: 800px;
    height: 1200px;
    overflow: hidden;
    background: var(--red-deep);
  }
  .cover {
    position: relative;
    width: 800px;
    height: 1200px;
    overflow: hidden;
    font-family: "Oswald", "Arial Narrow", sans-serif;
    color: var(--title-silver);
  }
  .cover-art {
    position: absolute;
    inset: 0;
    background:
      radial-gradient(ellipse 180px 320px at 440px 1130px, rgba(255, 70, 60, 0.85), rgba(229, 38, 43, 0) 100%),
      radial-gradient(ellipse 420px 380px at 200px 300px, rgba(190, 30, 34, 0.7), rgba(190, 30, 34, 0) 100%),
      linear-gradient(180deg, var(--red-mid) 0%, var(--red-dark) 45%, #3b0607 75%, var(--red-mid) 100%);
  }
  .cover-art::after {
    content: "";
    position: absolute;
    left: 360px;
    top: 800px;
    width: 150px;
    height: 400px;
    background: linear-gradient(180deg, rgba(255, 90, 80, 0.5), rgba(240, 40, 40, 0.9));
  }
  .author {
    position: absolute;
    top: 38px;
    left: 0;
    width: 100%;
    text-align: center;
    font-weight: 400;
    font-size: 70px;
    letter-spacing: 9px;
    color: var(--author-grey);
    line-height: 1;
  }
  .rule {
    position: absolute;
    height: 2px;
    background: var(--rule-grey);
  }
  .rule-top { top: 132px; left: 84px; width: 632px; }
  .title {
    position: absolute;
    top: 160px;
    left: 0;
    width: 100%;
    text-align: center;
    font-weight: 500;
    text-transform: uppercase;
    line-height: 1;
    color: var(--title-silver);
  }
  .title-lead {
    display: flex;
    justify-content: center;
    align-items: center;
    gap: 14px;
    font-size: 72px;
    height: 80px;
  }
  .title-lead .stars {
    font-size: 28px;
    letter-spacing: 6px;
  }
  .title-main {
    display: block;
    font-size: 196px;
    letter-spacing: 2px;
    margin-top: -4px;
  }
  .title-link {
    display: block;
    font-size: 96px;
    font-weight: 400;
    margin-top: -6px;
    letter-spacing: 2px;
  }
  .title-end {
    display: block;
    font-size: 196px;
    letter-spacing: 2px;
    margin-top: -10px;
  }
  .label-row {
    position: absolute;
    top: 733px;
    left: 84px;
    width: 632px;
    display: flex;
    align-items: center;
    gap: 18px;
  }
  .label-row .rule-seg {
    flex: 1;
    height: 2px;
    background: var(--rule-grey);
  }
  .label-row .label {
    font-weight: 400;
    font-size: 32px;
    letter-spacing: 5px;
    color: var(--author-grey);
    line-height: 1;
  }
</style>
</head>
<body>
  <main class="cover">
    <div class="cover-art" role="img" aria-label="Dark red photograph of a draped American flag with stars, above a glowing red corridor where a lone man walks away down a city street"></div>

    <p class="author">TOMAS REYVIK</p>
    <div class="rule rule-top"></div>

    <h1 class="title">
      <span class="title-lead"><span class="stars">★★</span>A<span class="stars">★★</span></span>
      <span class="title-main">Season</span>
      <span class="title-link">Of</span>
      <span class="title-end">Embers</span>
    </h1>

    <div class="label-row">
      <span class="rule-seg"></span>
      <span class="label">A NOVEL</span>
      <span class="rule-seg"></span>
    </div>
  </main>
</body>
</html>
```